OAKandRIVER Learning & Development
Business card, Letterhead & Compliment Slip design
Simple
Mara Hollings
Director
41 Fennick Row
Brenford
North Dunmere KX4 7RB
mhollings@oakandriverltd-example.co.uk
www.oakandriverltd-example.co.uk
Letterhead needs to be UK standard size A4 and used electronically, therefore, not too heavy on printer toner.
Compliment slip needs to be DL size which is 110mm x 220mm.
We are open to your ideas on this, it could be that the logo is on the front and all other details on reverse side.
We would like to see your ideas please.
Please see attached file for our logo, to be included in this design project. Many thanks.

```html
<!DOCTYPE html>
<html lang="en">
<head>
<meta charset="utf-8">
<title>Oak and River Learning &amp; Development – Stationery</title>
<link href="https://fonts.googleapis.com/css2?family=Roboto+Condensed:wght@700&family=Open+Sans:wght@400;600&display=swap" rel="stylesheet">
<style>
  :root{
    --bg:#2b2b2b;
    --orange:#f39a1c;
    --orange-light:#ffc36a;
    --orange-deep:#e07f00;
    --black:#151515;
    --charcoal:#262626;
    --white:#ffffff;
    --grey:#bdbdbd;
    --brand:"Roboto Condensed", Arial, sans-serif;
    --body:"Open Sans", Arial, sans-serif;
  }
  *{box-sizing:border-box;margin:0;padding:0}
  html,body{width:1200px;height:667px;overflow:hidden}
  body{background:var(--bg);position:relative;font-family:var(--body)}

  .brand-name{font-family:var(--brand);font-weight:700;line-height:1.15;text-align:center}

  /* business card front */
  .card-front{position:absolute;left:43px;top:48px;width:413px;height:250px;border-radius:18px;overflow:hidden;
    background:linear-gradient(160deg,var(--white) 0%,var(--orange-light) 28%,var(--orange) 55%,var(--orange-deep) 100%)}
  .card-front .brand-name{position:absolute;left:40px;right:40px;top:84px;font-size:24px;color:var(--white)}
  .card-front .web-strip{position:absolute;left:0;right:0;bottom:0;height:52px;background:var(--orange-deep);
    border-top:2px solid var(--orange-light);display:flex;align-items:center;justify-content:center;
    color:var(--white);font-size:12px;font-weight:600}

  /* business card back */
  .card-back{position:absolute;left:43px;top:336px;width:413px;height:293px;border-radius:14px;overflow:hidden;
    background:linear-gradient(180deg,var(--charcoal),var(--black))}
  .card-back .brand-name{position:absolute;left:20px;top:30px;width:180px;font-size:17px;color:var(--orange)}
  .card-back .name-panel{position:absolute;left:220px;top:0;right:0;height:136px;
    background:linear-gradient(180deg,var(--orange-light),var(--orange));padding:22px 16px}
  .card-back .person{font-family:var(--brand);font-weight:700;font-size:18px;color:var(--black)}
  .card-back .role{font-size:11px;color:var(--charcoal);margin-top:4px}
  .card-back .contacts{position:absolute;left:230px;top:150px;right:6px;list-style:none;color:var(--grey);font-size:7.5px;line-height:1.3}
  .card-back .contacts li{display:flex;align-items:flex-start;gap:6px;margin-bottom:6px;white-space:nowrap}
  .card-back .contacts svg{flex:none;width:10px;height:10px}

  /* brand lockup */
  .logo-lockup{position:absolute;left:852px;top:60px;width:276px}
  .logo-lockup .mark{width:46px;height:46px;border-radius:50%;background:var(--orange);margin:0 auto 14px}
  .logo-lockup .brand-name{font-size:28px;color:var(--white)}

  /* compliment slips (DL) */
  .slip{position:absolute;overflow:hidden;background:var(--white);box-shadow:0 6px 14px rgba(0,0,0,.45)}
  .slip .band-top{position:absolute;left:0;right:0;top:0;background:var(--black)}
  .slip .band-bottom{position:absolute;left:0;right:0;bottom:0;background:linear-gradient(180deg,var(--orange),var(--orange-deep))}
  .slip .brand-name{position:absolute;color:var(--black);font-size:18px}

  .slip-back{left:540px;top:310px;width:360px;height:180px}
  .slip-back .band-top{height:52px}
  .slip-back .band-bottom{height:52px}
  .slip-back .brand-name{left:0;right:0;top:58px}

  .slip-front{left:770px;top:420px;width:380px;height:190px}
  .slip-front .band-top{height:14px;background:var(--charcoal)}
  .slip-front .band-bottom{height:80px}
  .slip-front .brand-name{right:24px;top:36px;width:200px}
</style>
</head>
<body>

  <section class="card-front" aria-label="Business card front">
    <div class="brand-name">Oak and River Learning &amp; Development</div>
    <div class="web-strip">www.oakandriverltd-example.co.uk</div>
  </section>

  <section class="card-back" aria-label="Business card back">
    <div class="brand-name">Oak and River Learning &amp; Development</div>
    <div class="name-panel">
      <div class="person">Mara Hollings</div>
      <div class="role">Director</div>
    </div>
    <ul class="contacts">
      <li><svg viewBox="0 0 10 10"><path d="M5 0.5a3.2 3.2 0 0 1 3.2 3.2C8.2 6 5 9.5 5 9.5S1.8 6 1.8 3.7A3.2 3.2 0 0 1 5 0.5z" fill="#f39a1c"/><circle cx="5" cy="3.7" r="1.2" fill="#151515"/></svg><span>41 Fennick Row<br>Brenford North Dunmere KX4 7RB</span></li>
      <li><svg viewBox="0 0 10 10"><path d="M2 1l2 2-1 1.2c.6 1.2 1.6 2.2 2.8 2.8L7 6l2 2-1.3 1.3C4.5 9 1 5.5.7 2.3z" fill="#f39a1c"/></svg><span>Tel 01632 960 010</span></li>
      <li><svg viewBox="0 0 10 10"><rect x="2.5" y="0.5" width="5" height="9" rx="1" fill="#f39a1c"/></svg><span>Mob 07700 900 123</span></li>
      <li><svg viewBox="0 0 10 10"><rect x="1" y="3" width="8" height="5" fill="#f39a1c"/><rect x="2.5" y="1" width="5" height="2" fill="#f39a1c"/></svg><span>Fax 01632 960 011</span></li>
      <li><svg viewBox="0 0 10 10"><circle cx="5" cy="5" r="4" fill="none" stroke="#f39a1c" stroke-width="1.2"/><path d="M1 5h8M5 1v8" stroke="#f39a1c" stroke-width=".8"/></svg><span>www.oakandriverltd-example.co.uk</span></li>
      <li><svg viewBox="0 0 10 10"><rect x=".5" y="2" width="9" height="6" fill="#f39a1c"/><path d="M.5 2L5 5.5 9.5 2" fill="none" stroke="#151515" stroke-width=".8"/></svg><span>mhollings@oakandriverltd-example.co.uk</span></li>
    </ul>
  </section>

  <section class="logo-lockup" aria-label="Brand lockup">
    <div class="mark"></div>
    <div class="brand-name">Oak and River Learning &amp; Development</div>
  </section>

  <section class="slip slip-back" aria-label="Compliment slip reverse">
    <div class="band-top"></div>
    <div class="brand-name">Oak and River<br>Learning &amp; Development</div>
    <div class="band-bottom"></div>
  </section>

  <section class="slip slip-front" aria-label="Compliment slip front">
    <div class="band-top"></div>
    <div class="brand-name">Oak and River<br>Learning &amp; Development</div>
    <div class="band-bottom"></div>
  </section>

</body>
</html>
```